German Webagency needs fresh modern Design

Our website is 4 years old. We need an fresh modern website. All pics we used before are from customers or handmade by us. the new website should be clear with nice handling. please dont copy something from template websites. it would be great if you can surprise us with something great. its our first project here. don´t worry if i make a mistake in responding or briefing. after 20 years you can´t see the works of your own "designer" so we hope for help :-)
our existing site: www.tovankreativ.de
Target Market(s)
small and middle sized companys in germany
Number of Pages Required
4 page
Font styles to use
Colors
Designer to choose colors to be used in the design.
Requirements
Must have
- Responsive (sure we code it)
- Modern and big Font ..Headlines and Slider
- innovative..if you know something new..feel free to show
Nice to have
- the site with our works/refences should look great and later easy to handle when we code it or use wp.
- we like black and grey but if you have better ideas also feel free
Should not have
- a cup of coffe..laptop.. a pencil a handwritten font
- dont copy and modify templates from know websites..bad style

```html
<!DOCTYPE html>
<html lang="en">
<head>
<meta charset="utf-8">
<title>TovanKreativ – Web Agency</title>
<link rel="stylesheet" href="https://fonts.googleapis.com/css2?family=Hind:wght@400;500;600;700&family=Open+Sans:wght@400;600;700&family=Ubuntu:wght@500;700&display=swap">
<style>
:root{
  --ink:#2b2b2b;
  --muted:#555;
  --blue:#3a7fc1;
  --light:#f2f3f5;
  --dark:#333333;
  --darker:#222222;
  --white:#ffffff;
}
*{box-sizing:border-box;margin:0;padding:0}
html,body{width:1200px;height:3422px;overflow:hidden}
body{position:relative;background:var(--white);font-family:"Open Sans",sans-serif;color:var(--ink)}
.abs{position:absolute}
.heading{font-family:"Hind",sans-serif;font-weight:500;color:var(--ink);line-height:1.08}
.body-copy{font-size:9.5px;line-height:1.65;color:var(--muted)}
.btn{position:absolute;background:var(--blue);color:var(--white);font-size:8px;font-weight:700;letter-spacing:.5px;display:flex;align-items:center;justify-content:center;text-transform:uppercase}

/* hero */
.hero{left:0;top:0;width:1200px;height:662px;overflow:hidden;
  background:
    radial-gradient(ellipse 260px 340px at 90px 260px,#6d6258 0%,transparent 70%),
    radial-gradient(ellipse 320px 260px at 620px 420px,#7a7066 0%,transparent 70%),
    radial-gradient(ellipse 300px 380px at 1020px 300px,#4d443c 0%,transparent 70%),
    radial-gradient(ellipse 500px 200px at 600px 120px,#8c8a84 0%,transparent 70%),
    linear-gradient(180deg,#3c3631 0%,#2a2521 60%,#3a342e 100%)}
.hero::after{content:"";position:absolute;inset:0;background:rgba(0,0,0,.42)}
.brand{position:absolute;font-family:"Hind",sans-serif;font-weight:700;color:var(--white);font-size:32px;letter-spacing:-.5px;z-index:2}
.nav{position:absolute;left:634px;top:39px;display:flex;gap:27px;z-index:2}
.nav a{color:var(--white);font-size:10px;font-weight:700;text-decoration:none;text-transform:uppercase}
.nav-cta{position:absolute;left:926px;top:32px;width:122px;height:32px;border:2px solid var(--white);color:var(--white);font-size:10px;font-weight:700;display:flex;align-items:center;justify-content:center;z-index:2}
.hero-title{position:absolute;left:0;top:258px;width:1200px;text-align:center;font-family:"Hind",sans-serif;font-weight:600;font-size:64px;color:var(--white);z-index:2;line-height:1}
.hero-lead{position:absolute;left:240px;top:344px;width:720px;text-align:center;font-size:12px;line-height:1.9;color:var(--white);font-weight:600;z-index:2}
.hero-arrow{position:absolute;left:582px;top:612px;z-index:2}

/* services */
.services-title{left:216px;top:698px;font-size:41px;width:280px}
.services-lead{left:216px;top:898px;width:260px}
.service{position:absolute;left:588px;width:400px;height:120px}
.service .photo{position:absolute;left:0;top:0;width:114px;height:114px;border-radius:50%;border:5px solid #fff;box-shadow:0 0 0 1px #d8d8d8}
.service h3{position:absolute;left:151px;top:2px;font-family:"Hind",sans-serif;font-weight:600;font-size:16px;color:var(--ink)}
.service p{position:absolute;left:151px;top:26px;width:240px}
.service .btn{left:151px;top:88px;width:94px;height:24px}

/* vision */
.vision{left:0;top:1152px;width:1200px;height:297px;background:var(--light)}
.vision .photo{position:absolute;left:0;top:0;width:600px;height:297px;
  background:linear-gradient(180deg,#8796a6 0%,#c4ccd4 30%,#e6e8ea 52%,#b9b6ae 66%,#7d7a72 80%,#5a5852 100%)}
.vision-title{left:661px;top:30px;font-size:41px;width:340px}
.vision-copy{left:661px;top:140px;width:320px}
.vision .btn{left:667px;top:232px;width:96px;height:25px}

/* work */
.section-title{position:absolute;left:0;width:1200px;text-align:center;font-family:"Hind",sans-serif;font-weight:500;font-size:40px;color:var(--ink)}
.filters{position:absolute;left:0;top:1552px;width:1200px;display:flex;justify-content:center;gap:18px;font-size:8px;font-weight:700;text-transform:uppercase}
.filters .active{color:var(--blue)}
.work-grid{position:absolute;left:214px;top:1594px;width:769px;height:402px;display:grid;grid-template-columns:repeat(4,1fr);grid-template-rows:repeat(2,1fr)}
.mock{background:var(--page);padding:8px;display:flex;flex-direction:column;gap:6px;border:1px solid rgba(0,0,0,.08);overflow:hidden}
.mock-bar{height:12px;background:var(--bar);display:flex;justify-content:flex-end;align-items:center;gap:4px;padding-right:6px}
.mock-bar i{width:14px;height:3px;background:rgba(255,255,255,.6)}
.mock-hero{height:72px;background:var(--accent)}
.mock-row{display:flex;gap:5px;height:38px}
.mock-row i{flex:1;background:var(--tint)}
.mock-lines b{display:block;height:4px;background:var(--line);margin-bottom:5px}
.work-more{background:var(--darker);position:relative}
.work-more span{position:absolute;left:12px;bottom:22px;color:var(--white);font-family:"Hind",sans-serif;font-weight:600;font-size:21px;line-height:1;text-transform:uppercase}
.work-more svg{position:absolute;right:12px;top:118px}

/* clients */
.clients{left:0;top:2041px;width:1200px;height:183px;background:var(--light)}
.client-row{position:absolute;left:214px;top:72px;width:772px;display:flex;justify-content:space-between;align-items:center}
.client{font-family:"Hind",sans-serif;font-weight:700;font-size:26px;color:#4a4a4a;display:flex;align-items:center;gap:8px}
.client .mark{width:22px;height:22px;border-radius:50%;background:#4a4a4a}

/* testimonial */
.avatar{left:525px;top:2352px;width:150px;height:150px;border-radius:50%;background:radial-gradient(circle at 50% 40%,#9a6a5e 0%,#5c3432 55%,#2a1a1c 100%)}
.t-name{left:0;top:2526px;width:1200px;text-align:center;font-family:"Hind",sans-serif;font-weight:600;font-size:20px}
.t-company{left:0;top:2553px;width:1200px;text-align:center;font-size:10px;font-weight:600}
.t-quote{left:440px;top:2584px;width:320px;text-align:center}
.dots{position:absolute;left:572px;top:2674px;display:flex;gap:7px}
.dots i{width:12px;height:12px;border-radius:50%;border:2px solid var(--ink)}
.dots i.on{background:var(--ink)}

/* contact */
.contact{left:0;top:2730px;width:1200px;height:418px;
  background:linear-gradient(180deg,#8aa4bc 0%,#6f9a78 40%,#54804a 70%,#3f5e38 100%)}
.contact::after{content:"";position:absolute;inset:0;background:rgba(38,80,140,.5)}
.contact-title{position:absolute;left:0;top:24px;width:1200px;text-align:center;font-family:"Ubuntu",sans-serif;font-weight:700;font-size:38px;color:var(--white);z-index:2}
.field{position:absolute;background:var(--white);font-size:8px;color:#555;padding:7px 8px;z-index:2}
.submit{position:absolute;left:536px;top:347px;width:123px;height:32px;border:1px solid var(--white);color:var(--white);font-size:8px;font-weight:700;display:flex;align-items:center;justify-content:center;z-index:2}

/* footer */
.footer{left:0;top:3148px;width:1200px;height:274px;background:var(--dark);color:var(--white)}
.footer .brand{left:148px;top:30px;font-size:26px}
.f-contact{position:absolute;left:148px;display:flex;align-items:flex-start;gap:20px;font-size:9.5px;line-height:1.55}
.f-contact svg{flex:none}
.f-head{position:absolute;top:46px;font-size:10px;font-weight:700;text-transform:uppercase;padding-bottom:5px;border-bottom:2px solid var(--blue)}
.f-links{position:absolute;font-size:10px;line-height:2.1}
.f-about{position:absolute;left:739px;top:88px;width:310px;font-size:9px;line-height:1.6;font-weight:600}
.socials{position:absolute;left:739px;top:166px;display:flex;gap:9px}
.socials i{width:20px;height:20px;border-radius:50%;background:var(--white)}
.copyright{position:absolute;left:0;top:242px;width:1200px;text-align:center;font-size:7px;letter-spacing:.3px;text-transform:uppercase}
</style>
</head>
<body>

<header class="hero abs" role="img" aria-label="Photo of a film crew and onlookers at an outdoor event">
  <div class="brand" style="left:148px;top:22px">tovankreativ</div>
  <nav class="nav">
    <a>Home</a><a>Services</a><a>Portfolio</a><a>About us</a>
  </nav>
  <div class="nav-cta">GET IN TOUCH</div>
  <h1 class="hero-title">We are TovanKreativ</h1>
  <p class="hero-lead">TovanKreativ is a full service web agency who specialise in responsive web design, web development,<br>digital marketing and graphic design. We believe in creating lasting impressions and optimising your business.</p>
  <svg class="hero-arrow" width="36" height="20" viewBox="0 0 36 20"><path d="M2 2 L18 17 L34 2" fill="none" stroke="#fff" stroke-width="2.5"/></svg>
</header>

<section>
  <h2 class="heading services-title abs">Outstanding web design, marketing and branding</h2>
  <p class="body-copy services-lead abs">We plan, design and build brands that grow with your company and make every first contact count.</p>

  <div class="service" style="top:703px">
    <div class="photo" role="img" aria-label="Photo of a web design workspace with screens" style="background:radial-gradient(circle at 45% 40%,#f0f2f5 0%,#a9b2be 50%,#4a5260 100%)"></div>
    <h3>Web Design</h3>
    <p class="body-copy">Clean, fast and responsive websites that work on every screen and are easy for your team to update.</p>
    <div class="btn">Find out more</div>
  </div>
  <div class="service" style="top:849px">
    <div class="photo" role="img" aria-label="Photo of a marketing planning session at a whiteboard" style="background:radial-gradient(circle at 45% 40%,#f7f4ee 0%,#ddd2c4 50%,#9a8874 100%)"></div>
    <h3>Digital Marketing</h3>
    <p class="body-copy">Search, social and newsletter campaigns that bring the right visitors and turn them into customers.</p>
    <div class="btn">Find out more</div>
  </div>
  <div class="service" style="top:995px">
    <div class="photo" role="img" aria-label="Photo of a graphic designer working at a monitor" style="background:radial-gradient(circle at 45% 40%,#e2ddd8 0%,#8a7a70 50%,#2e2826 100%)"></div>
    <h3>Graphic Design</h3>
    <p class="body-copy">Logos, print and packaging with a clear voice that makes your business recognisable at a glance.</p>
    <div class="btn">Find out more</div>
  </div>
</section>

<section class="vision abs">
  <div class="photo" role="img" aria-label="Photo of a private jet and a helicopter on an airfield"></div>
  <h2 class="heading vision-title abs">Building visions<br>for 18 years</h2>
  <p class="body-copy vision-copy abs">Since 1998 we have helped small and medium sized companies across Germany find their voice online. We listen, plan with care and deliver work that lasts, from the first sketch to the final launch.</p>
  <div class="btn">More about us</div>
</section>

<section>
  <h2 class="section-title" style="top:1486px">Our work</h2>
  <div class="filters"><span>All</span><span class="active">Web design</span><span>Graphic design</span><span>Marketing</span></div>
  <div class="work-grid">
    <div class="mock" style="--page:#f4f1ec;--bar:#3b2a1c;--accent:#b88a52;--tint:#d9c7ae;--line:#c9c2b8">
      <div class="mock-bar"><i></i><i></i><i></i></div>
      <div class="mock-hero" role="img" aria-label="Website project for a restaurant, interior photo"></div>
      <div class="mock-row"><i></i><i></i><i></i><i></i></div>
      <div class="mock-lines"><b></b><b></b><b style="width:60%"></b></div>
    </div>
    <div class="mock" style="--page:#ffffff;--bar:#1f4f8f;--accent:#c98a3a;--tint:#d7dde6;--line:#d6d6d6">
      <div class="mock-bar"><i></i><i></i><i></i></div>
      <div class="mock-hero" role="img" aria-label="Website project for an event venue, stage photo"></div>
      <div class="mock-row"><i></i><i></i><i></i></div>
      <div class="mock-lines"><b></b><b style="width:80%"></b><b style="width:55%"></b></div>
    </div>
    <div class="mock" style="--page:#1f1f1f;--bar:#000000;--accent:#7a5a50;--tint:#3c3c3c;--line:#4a4a4a">
      <div class="mock-bar"><i></i><i></i><i></i></div>
      <div class="mock-hero" role="img" aria-label="Website project for a cosmetics brand, beauty photo"></div>
      <div class="mock-row"><i></i><i></i><i></i></div>
      <div class="mock-lines"><b></b><b style="width:70%"></b><b style="width:45%"></b></div>
    </div>
    <div class="mock" style="--page:#f3f3f3;--bar:#2b2b2b;--accent:#8ea878;--tint:#dcdcdc;--line:#cfcfcf">
      <div class="mock-bar"><i></i><i></i><i></i></div>
      <div class="mock-hero" role="img" aria-label="Website project for a cosmetics shop, store interior photo"></div>
      <div class="mock-row"><i></i><i></i><i></i><i></i></div>
      <div class="mock-lines"><b></b><b></b><b style="width:50%"></b></div>
    </div>
    <div class="mock" style="--page:#ffffff;--bar:#3f6a24;--accent:#7aa24a;--tint:#dfe8d4;--line:#d4d4d4">
      <div class="mock-bar"><i></i><i></i><i></i></div>
      <div class="mock-hero" role="img" aria-label="Website project for an outdoor club, landscape photo"></div>
      <div class="mock-row"><i></i><i></i><i></i></div>
      <div class="mock-lines"><b></b><b style="width:75%"></b><b style="width:60%"></b></div>
    </div>
    <div class="mock" style="--page:#ececec;--bar:#1f3f8a;--accent:#6f7c8c;--tint:#cfd6e0;--line:#c7c7c7">
      <div class="mock-bar"><i></i><i></i><i></i></div>
      <div class="mock-hero" role="img" aria-label="Website project for a car dealer, vehicle photo"></div>
      <div class="mock-row"><i></i><i></i><i></i><i></i></div>
      <div class="mock-lines"><b></b><b style="width:85%"></b><b style="width:50%"></b></div>
    </div>
    <div class="mock" style="--page:#f2f2f2;--bar:#2d2d2d;--accent:#c9a33a;--tint:#d8d8d8;--line:#cccccc">
      <div class="mock-bar"><i></i><i></i><i></i></div>
      <div class="mock-hero" role="img" aria-label="Website project for a construction company, machinery photo"></div>
      <div class="mock-row"><i></i><i></i><i></i></div>
      <div class="mock-lines"><b></b><b></b><b style="width:65%"></b></div>
    </div>
    <div class="work-more">
      <span>View our<br>portfolio</span>
      <svg width="14" height="26" viewBox="0 0 14 26"><path d="M2 2 L12 13 L2 24" fill="none" stroke="#fff" stroke-width="2"/></svg>
    </div>
  </div>
</section>

<section class="clients abs">
  <div class="client-row">
    <div class="client">Wildcat</div>
    <div class="client">Lumen</div>
    <div class="client">Stepwise</div>
    <div class="client">falke&amp;co</div>
    <div class="client"><span class="mark"></span>Mono</div>
  </div>
</section>

<section>
  <h2 class="section-title" style="top:2264px">What our clients have to say</h2>
  <div class="avatar abs" role="img" aria-label="Portrait photo of the client"></div>
  <div class="t-name abs">Clara Winter</div>
  <div class="t-company abs">Winter Cosmetics and Beauty</div>
  <p class="body-copy t-quote abs">Working with the team was easy from day one. They understood our brand, kept every deadline and delivered a website our customers love to use.</p>
  <div class="dots"><i></i><i class="on"></i><i></i></div>
</section>

<section class="contact abs" role="img" aria-label="Photo of cows grazing on an alpine meadow">
  <h2 class="contact-title">Let’s work together</h2>
  <div class="field" style="left:312px;top:98px;width:281px;height:30px">Your name</div>
  <div class="field" style="left:607px;top:98px;width:283px;height:30px">Your email</div>
  <div class="field" style="left:312px;top:144px;width:281px;height:30px">Your number</div>
  <div class="field" style="left:607px;top:144px;width:283px;height:30px">Your company</div>
  <div class="field" style="left:312px;top:190px;width:578px;height:143px">What do you have in mind?</div>
  <div class="submit">SUBMIT</div>
</section>

<footer class="footer abs">
  <div class="brand">tovankreativ</div>

  <div class="f-contact" style="top:92px">
    <svg width="14" height="16" viewBox="0 0 14 16"><path d="M7 1a5 5 0 0 1 5 5c0 4-5 9-5 9S2 10 2 6a5 5 0 0 1 5-5z" fill="#fff"/><circle cx="7" cy="6" r="2" fill="#333"/></svg>
    <span>Lindenweg 14, 34567 Auental Germany</span>
  </div>
  <div class="f-contact" style="top:130px">
    <svg width="14" height="16" viewBox="0 0 14 16"><rect x="3" y="0" width="8" height="16" rx="1.5" fill="#fff"/><rect x="4.5" y="2" width="5" height="10" fill="#333"/></svg>
    <span>05600 - 123 456</span>
  </div>
  <div class="f-contact" style="top:170px">
    <svg width="16" height="12" viewBox="0 0 16 12"><rect x="0" y="0" width="16" height="12" fill="#fff"/><path d="M0 0 L8 7 L16 0" fill="none" stroke="#333" stroke-width="1.5"/></svg>
    <span>Jonas Tovan j.tovan@tovankreativ.de<br>Lukas Feldmann l.feldmann@tovankreativ.de</span>
  </div>

  <div class="f-head" style="left:515px">Company</div>
  <div class="f-links" style="left:515px;top:92px">Home<br>Services<br>Portfolio</div>
  <div class="f-links" style="left:598px;top:92px">About Us<br>Contact</div>

  <div class="f-head" style="left:739px">About us</div>
  <p class="f-about">We are a small full service agency from northern Hesse. For twenty years we have designed websites, brands and campaigns for companies who value clear work and honest advice.</p>
  <div class="socials"><i></i><i></i><i></i><i></i></div>

  <div class="copyright">Copyright ©TovanKreativ 2015. All rights reserved.</div>
</footer>

</body>
</html>
```